Dog Snacks brand needs a new packaging design

Dear Designers,

We are looking for a packaging expert to design our new line of Dog Snacks which contain a relaxing hemp extract (CBD).

Our company is already selling various relaxing cat & dog products , and we would like this new design to reflect the same "style & feeling" as our current products (see attached instructions).

Technical aspects:
- The packaging is a Stand Up Pouch (12x18.5x7cm - see attached instructions).
- Please follow technical guidelines from printer (see attached instructions).
- The packaging will contain 120g of high-quality, semi-moist dog snacks.
- We will be designing 3 differents variations for 3 different flavours: Chicken, Beef & Liver.
- The packaging will be printed with a matt finish.

Design aspects:
- The design should be compatible with our brand identity (i.e. fluffly, pure, relaxing, positive, clean & natural).
- Soft/rounded shapes are preferred.
- Please use our brand's colors (#3BA384, White & Black).
- Please use our company logo (see attached instructions).
- The design also needs to convey a strong sense of professionalism as we are an animal "healthcare" brand.
- If you want to include a dog picture, we would prefer you to use a picture of our official brand ambassador (see attached instructions).
- We have attached a number of packaging examples which we like a lot. (see attached instructions). Please only use those as general inspiration.
- Only original work (no plagiarism will be accepted).

Please don't hesitate to send us a message if you have any questions about the brand, the product or the design requirements.

We look forward to seeing your designs & working on this together !

Thanks & regards,
Marcus

Dog owners

Pet Care

Sans Serif

• Please see project description.

```html
<!DOCTYPE html>
<html lang="en">
<head>
<meta charset="utf-8">
<title>Verdalis For Animals – CBD Treats Pouch</title>
<link rel="stylesheet" href="https://fonts.googleapis.com/css2?family=Montserrat:wght@300;400&family=Roboto+Slab:wght@300;400;800&display=swap">
<style>
  :root {
    --brand-green: #3ba384;
    --pouch-black: #0b0b0b;
    --pouch-grey: #2e2e2e;
    --white: #ffffff;
    --backdrop: #d9d9d9;
    --photo-light: #eef0f1;
    --photo-mid: #b9bcbf;
  }
  * { margin: 0; padding: 0; box-sizing: border-box; }
  html, body {
    width: 1200px; height: 835px; overflow: hidden;
    background: var(--backdrop);
  }
  .canvas {
    position: relative; width: 1200px; height: 835px;
    background: linear-gradient(180deg, #e4e4e4 0%, var(--backdrop) 100%);
  }
  .pouch {
    position: absolute; left: 355px; top: 22px;
    width: 490px; height: 790px;
    border-radius: 12px 12px 6px 6px;
    background: linear-gradient(200deg, var(--pouch-grey) 0%, #161616 35%, var(--pouch-black) 60%);
    overflow: hidden;
  }
  .pouch__zipper {
    position: absolute; left: 0; right: 0; top: 78px; height: 6px;
    border-top: 1px solid #3a3a3a; border-bottom: 1px solid #3a3a3a;
  }
  .pouch__seal {
    position: absolute; left: 0; right: 0; top: 18px; height: 1px; background: #333;
  }
  .brand {
    position: absolute; left: 37px; top: 40px; width: 275px;
    text-align: center;
  }
  .brand__dot {
    display: block; width: 44px; height: 44px; margin: 0 auto 36px;
    border-radius: 50%; background: var(--brand-green);
  }
  .brand__name {
    font-family: "Roboto Slab", serif; font-weight: 300;
    font-size: 50px; line-height: 1; color: var(--white); letter-spacing: 0.5px;
  }
  .brand__tagline {
    position: absolute; left: 37px; top: 196px; width: 275px; text-align: right;
    font-family: "Roboto Slab", serif; font-weight: 400;
    font-size: 23px; color: var(--brand-green);
  }
  .vertical {
    position: absolute; writing-mode: vertical-rl; transform: rotate(180deg);
    white-space: nowrap; line-height: 1;
  }
  .product-name {
    left: 36px; bottom: 90px;
    font-family: "Roboto Slab", serif; font-weight: 800;
    font-size: 42px; color: var(--brand-green); letter-spacing: 1px;
  }
  .product-type {
    left: 92px; bottom: 88px;
    font-family: "Roboto Slab", serif; font-weight: 300;
    font-size: 34px; color: var(--white);
  }
  .product-dose {
    left: 134px; bottom: 88px;
    font-family: "Montserrat", sans-serif; font-weight: 300;
    font-size: 15px; color: var(--brand-green); letter-spacing: 0.5px;
  }
  .benefits {
    position: absolute; left: 54px; top: 719px; list-style: none;
    font-family: "Montserrat", sans-serif; font-weight: 400;
    font-size: 9.5px; color: #d6d6d6; line-height: 14px;
  }
  .benefits li::before {
    content: ""; display: inline-block; width: 5px; height: 5px; margin-right: 7px;
    border-radius: 50%; background: #555; vertical-align: middle;
  }
  .pet-photo {
    position: absolute; left: 200px; top: 300px; width: 290px; height: 490px;
    border-radius: 150px 0 0 0;
    background: radial-gradient(ellipse at 55% 45%, var(--photo-light) 0%, #d4d6d8 55%, var(--photo-mid) 100%);
  }
  .net-weight {
    position: absolute; left: 193px; top: 764px;
    font-family: "Montserrat", sans-serif; font-weight: 400;
    font-size: 19px; color: var(--brand-green);
  }
</style>
</head>
<body>
<main class="canvas">
  <article class="pouch">
    <div class="pouch__seal"></div>
    <div class="pouch__zipper"></div>

    <div class="pet-photo" role="img" aria-label="Black and white photo of the brand's wrinkled dog ambassador looking upward"></div>

    <header class="brand">
      <span class="brand__dot"></span>
      <h1 class="brand__name">VERDALIS</h1>
    </header>
    <p class="brand__tagline">For Animals</p>

    <h2 class="vertical product-name">VERDALICIOUS</h2>
    <p class="vertical product-type">CBD TREATS</p>
    <p class="vertical product-dose">CBD 250MG &nbsp;|&nbsp; 0% THC</p>

    <ul class="benefits">
      <li>SUPPORT</li>
      <li>CALM</li>
      <li>EASE</li>
    </ul>

    <p class="net-weight">120g</p>
  </article>
</main>
</body>
</html>
```